We need a completed book cover (front and back) for a Christian devotional book titled "Rooted in Quiet Light: Walking as an Oak & LAMP Follower" by Dr. Glen Marsh. The publishing company should be "Oak & Lamp" (https://oaklamp-press.net). This will be for small groups to go through together daily to understand how to grow as a Christian as a part of the family of God. I'm attaching the Oak & Lamp logo and the introduction to the book.
Main themes include navigating today’s culture, understanding and using our spiritual gifts, and experiencing joy in community.

```html
<!DOCTYPE html>
<html lang="en">
<head>
<meta charset="utf-8">
<title>Rooted in Quiet Light — Book Cover</title>
<link href="https://fonts.googleapis.com/css2?family=Montserrat:wght@300;400;500;700;900&display=swap" rel="stylesheet">
<style>
  :root{
    --page:#ffffff;
    --navy:#04577b;
    --ink:#1b1d1c;
    --back-bg:#cbcfbf;
    --back-bg-deep:#bcc2ad;
    --mist:#dfe1d3;
    --sage:#a9b295;
    --forest:#5c6b45;
    --placeholder:#9c9c9c;
    --frame:#7d7f76;
    --white:#ffffff;
  }
  *{margin:0;padding:0;box-sizing:border-box}
  html,body{width:1200px;height:900px;overflow:hidden;background:var(--page)}
  body{font-family:"Montserrat",Arial,sans-serif;color:var(--ink);position:relative}

  .cover{position:absolute;left:65px;top:64px;width:1071px;height:772px}

  .back{position:absolute;left:0;top:0;width:556px;height:715px;
    background:linear-gradient(180deg,var(--back-bg) 0%,var(--back-bg-deep) 100%)}

  .back-title{position:absolute;left:155px;top:42px;width:194px;height:106px}
  .back-blurb{position:absolute;left:25px;top:160px;width:461px;font-size:11.2px;font-weight:300;
    line-height:14.3px;text-align:justify}
  .back-blurb p+p{margin-top:6px}

  .author-rule{position:absolute;left:25px;top:374px;width:461px;display:flex;align-items:center;gap:12px}
  .author-rule::before,.author-rule::after{content:"";flex:1;height:1px;background:var(--navy)}
  .author-rule span{font-size:21px;font-weight:500;white-space:nowrap}

  .author-photo{position:absolute;left:25px;top:422px;width:136px;height:152px;background:var(--placeholder)}
  .author-bio{position:absolute;left:174px;top:425px;width:304px;font-size:11.2px;font-weight:300;
    line-height:14.3px;text-align:justify}
  .code-frame{position:absolute;left:290px;top:589px;width:190px;height:109px;border:1px solid var(--frame)}

  .publisher-back{position:absolute;left:52px;top:640px;width:120px;text-align:center;
    font-size:14px;font-weight:700;color:var(--ink);display:flex;flex-direction:column;align-items:center;gap:6px}
  .publisher-back i{display:block;width:22px;height:22px;border-radius:50%;background:var(--ink)}

  .spine{position:absolute;left:514px;top:0;width:42px;height:715px;border-right:1px solid rgba(4,87,123,.25)}
  .spine-author,.spine-title{position:absolute;left:50%;white-space:nowrap;transform-origin:center}
  .spine-author{top:180px;font-size:15px;font-weight:500;transform:translate(-50%,-50%) rotate(-90deg);color:var(--ink)}
  .spine-title{top:464px;font-size:16px;font-weight:900;letter-spacing:3.6px;color:var(--navy);
    transform:translate(-50%,-50%) rotate(-90deg)}

  .front{position:absolute;left:557px;top:0;width:514px;height:715px;overflow:hidden}
  .front-scene{position:absolute;inset:0;
    background:linear-gradient(180deg,var(--mist) 0%,var(--mist) 30%,var(--sage) 65%,var(--forest) 100%)}
  .front-title{position:absolute;left:55px;top:44px;width:403px;height:212px}
  .front-subtitle{position:absolute;left:0;width:100%;top:316px;text-align:center;font-size:16.5px;
    font-weight:500;letter-spacing:1px;color:var(--ink)}

  .band{position:absolute;left:0;top:715px;width:1071px;height:57px;background:var(--navy)}
  .publisher-spine{position:absolute;left:495px;top:13px;width:80px;text-align:center;color:var(--white);
    font-size:9px;font-weight:700;white-space:nowrap;display:flex;flex-direction:column;align-items:center;gap:4px}
  .publisher-spine i{display:block;width:14px;height:14px;border-radius:50%;background:var(--white)}
  .front-author{position:absolute;left:557px;width:514px;top:8px;text-align:center;color:var(--white);
    font-size:34px;font-weight:500}
</style>
</head>
<body>
<div class="cover">

  <section class="back">
    <svg class="back-title" viewBox="0 0 194 106" aria-label="Rooted in Quiet Light">
      <g fill="var(--navy)" font-family="Montserrat, Arial, sans-serif" font-weight="900">
        <text x="0" y="29" font-size="35" textLength="194" lengthAdjust="spacing">ROOTED</text>
        <text x="0" y="66" font-size="34" textLength="194" lengthAdjust="spacing">IN QUIET</text>
        <text x="0" y="104" font-size="38" textLength="194" lengthAdjust="spacing">LIGHT</text>
      </g>
    </svg>

    <div class="back-blurb">
      <p>Lorem ipsum dolor sit amet, consectetuer adipiscing elit, sed diam nonummy nibh euismod tincidunt ut laoreet dolore magna aliquam erat volutpat. Ut wisi enim ad minim veniam, quis nostrud exerci tation ullamcorper suscipit lobortis nisl ut aliquip ex ea commodo consequat. Duis autem vel eum iriure dolor in hendrerit in vulputate velit esse molestie consequat, vel illum dolore eu feugiat nulla facilisis at vero eros et accumsan et iusto odio dignissim qui Lorem ipsum dolor sit amet, consectetuer adipiscing elit, sed diam nonummy nibh euismod tincidunt ut laoreet dolore magna aliquam erat volutpat. Ut wisi enim ad minim veniam, quis nostrud exerci tation ullamcorper suscipit lobortis nisl ut aliquip ex ea commodo consequat. Duis autem vel eum iriure dolor in hendrerit in vulputate velit esse molestie consequat, vel illum dolore eu feugiat nulla facilisis at vero eros et accumsan et iusto odio dignissim qui</p>
      <p>Lorem ipsum dolor sit amet, consectetuer adipiscing elit, sed diam nonummy nibh euismod tincidunt ut laoreet dolore magna aliquam erat volutpat. Ut wisi</p>
    </div>

    <div class="author-rule"><span>Dr. Glen Marsh</span></div>

    <div class="author-photo" role="img" aria-label="Author portrait placeholder"></div>
    <p class="author-bio">Lorem ipsum dolor sit amet, consectetuer adipiscing elit, sed diam nonummy nibh euismod tincidunt ut laoreet dolore magna aliquam erat volutpat. Ut wisi enim ad minim veniam, quis nostrud exerci tation ullamcorper suscipit lobortis nisl ut aliquip ex ea commodo consequat. Duis autem vel eum iriure dolor in hendrerit in vulputate velit esse molestie consequat, vel illum dolore eu feugiat nulla facilisis at vero eros et accumsan et iusto odio dignissim qui Lorem ipsum dolor sit amet, consectetuer adipiscing elit, sed diam</p>

    <div class="code-frame"></div>

    <div class="publisher-back"><i></i><span>Oak &amp; Lamp</span></div>
  </section>

  <div class="spine">
    <span class="spine-author">Dr. Glen Marsh</span>
    <span class="spine-title">ROOTED IN QUIET LIGHT</span>
  </div>

  <section class="front">
    <div class="front-scene" role="img" aria-label="Cover photograph: misty forest with a stone path"></div>
    <svg class="front-title" viewBox="0 0 403 212" aria-label="Rooted in Quiet Light">
      <g fill="var(--navy)" font-family="Montserrat, Arial, sans-serif" font-weight="900">
        <text x="0" y="58" font-size="74" textLength="403" lengthAdjust="spacing">ROOTED</text>
        <text x="0" y="136" font-size="72" textLength="403" lengthAdjust="spacing">IN QUIET</text>
        <text x="0" y="210" font-size="74" textLength="403" lengthAdjust="spacing">LIGHT</text>
      </g>
    </svg>
    <p class="front-subtitle">WALKING AS AN OAK &amp; LAMP FOLLOWER</p>
  </section>

  <div class="band">
    <div class="publisher-spine"><i></i><span>Oak &amp; Lamp</span></div>
    <p class="front-author">Dr. Glen Marsh</p>
  </div>

</div>
</body>
</html>
```